Travel site flyer required

We have got a website that needs promoting.

www.farebrook.co.uk is the site and I'd like to have a catchy flyer that will draw people into going to visit the site.

here's a bit more about what our site does.

our site shares information on where to find bargain flights & holidays. We don't actually provide the deals but we offer a free service to help people finding amazing promotions.

Industry/Entity Type

Travel

Requirements
Must have
• somewhere at the bottom of the flyer a small recycling bin logo and request to dispose of this flyer responsibly.

```html
<!DOCTYPE html>
<html lang="en">
<head>
<meta charset="utf-8">
<title>Farebrook.co.uk – Travel Deals Flyer</title>
<link rel="stylesheet" href="https://fonts.googleapis.com/css2?family=Arimo:wght@400;700&display=swap">
<style>
  :root {
    --magenta: #b0198c;
    --magenta-soft: #e07ad0;
    --white: #ffffff;
    --ink: #111111;
    --sea: #3aa5b0;
    --hill: #2f4a2c;
    --recycle: #27b43a;
  }
  * { box-sizing: border-box; margin: 0; padding: 0; }
  html, body { width: 927px; height: 1200px; overflow: hidden; }
  body { font-family: "Arimo", Arial, sans-serif; color: var(--ink); }

  .flyer {
    position: relative;
    width: 927px;
    height: 1200px;
    overflow: hidden;
  }
  .backdrop {
    position: absolute; inset: 0;
    background:
      linear-gradient(180deg, #cdd6dc 0%, #6b8a78 12%, var(--hill) 35%, transparent 36%),
      linear-gradient(90deg, var(--sea) 0%, #4fb9c4 30%, #6aa4a8 60%, var(--hill) 85%, #263d22 100%);
  }

  .sheet {
    position: absolute;
    left: 105px; top: 49px;
    width: 710px; height: 1099px;
    background: var(--white);
  }

  .band {
    position: absolute; left: 0; width: 100%;
    background: var(--magenta);
    color: var(--white);
    white-space: nowrap;
  }
  .band--intro {
    top: 0; height: 121px;
    padding: 11px 0 0 13px;
    font-size: 17px; line-height: 21.8px;
    letter-spacing: 0.15px;
  }
  .band--promise {
    top: 998px; height: 101px;
    display: flex; align-items: center; justify-content: center;
    text-align: center;
    font-size: 27px; line-height: 33px;
    letter-spacing: 0.2px;
  }

  .brand {
    position: absolute; left: 0; width: 100%; top: 160px;
    text-align: center;
    font-weight: 700;
    font-size: 58px;
    letter-spacing: 1px;
    color: var(--magenta);
  }

  .deal { position: absolute; }
  .deal__visual {
    display: block;
    box-shadow: 3px 3px 4px rgba(0,0,0,.35);
  }
  .deal__caption {
    font-size: 17px; line-height: 22px;
    margin-top: 10px;
    white-space: nowrap;
  }

  .deal--hotel { left: 61px; top: 250px; }
  .deal--hotel .deal__visual { width: 225px; height: 151px; background: linear-gradient(135deg, #8a5a2e, #c9a872 50%, #5b3a6e); }
  .deal--hotel .deal__caption { margin-left: -10px; }

  .deal--australia { left: 385px; top: 250px; }
  .deal--australia .deal__visual { width: 226px; height: 151px; background: linear-gradient(180deg, #1c4fcf, #4f86e6 55%, #1a3fb0); }
  .deal--australia .deal__caption { margin-left: -50px; }

  .deal--jersey { left: 61px; top: 449px; }
  .deal--jersey .deal__visual { width: 225px; height: 142px; background: linear-gradient(180deg, #3f8fe0 0%, #1f6fc4 40%, #6b9b55 70%, #a9a49a 100%); }
  .deal--jersey .deal__caption { margin-left: -3px; margin-top: 19px; }

  .deal--theatre { left: 386px; top: 449px; }
  .deal--theatre .deal__visual { width: 225px; height: 150px; background: linear-gradient(120deg, #0c2a08, #3fb82a 45%, #143a0f 70%, #f2efe8); }
  .deal--theatre .deal__caption { margin-left: -50px; margin-top: 11px; }

  .deal--savings { left: 193px; top: 671px; }
  .deal--savings .deal__visual { width: 329px; height: 193px; background: radial-gradient(circle at 65% 45%, #f6c8ee, var(--magenta-soft) 40%, #c22fae 100%); }
  .deal--savings .deal__caption { margin-top: 10px; line-height: 22px; }

  .dispose-note {
    position: absolute; right: 84px; top: 1166px;
    font-size: 14px; line-height: 18px;
    color: var(--white);
    white-space: nowrap;
  }
  .recycle {
    position: absolute; left: 853px; top: 1148px;
    width: 56px; height: 48px;
  }
</style>
</head>
<body>
<div class="flyer">
  <div class="backdrop" role="img" aria-label="Coastal landscape with turquoise sea, sandy beach and green wooded hills"></div>

  <main class="sheet">
    <p class="band band--intro">The aim of our site is to offer people the visibility of the best travel deals on<br>the web. On a regular basis, we post amazing deals &amp; will show you how you<br>can book these deals. Farebrook.co.uk is completely FREE and does not<br>charge any commission. We offer you direct links to these amazing deals.</p>

    <h1 class="brand">farebrook.co.uk</h1>

    <figure class="deal deal--hotel">
      <div class="deal__visual" role="img" aria-label="Hotel bedroom with double bed and purple headboard"></div>
      <figcaption class="deal__caption">Restwell Inn rooms from £29</figcaption>
    </figure>

    <figure class="deal deal--australia">
      <div class="deal__visual" role="img" aria-label="Sydney harbour opera house under a blue sky"></div>
      <figcaption class="deal__caption">Win a dream holiday for 4 to Australia</figcaption>
    </figure>

    <figure class="deal deal--jersey">
      <div class="deal__visual" role="img" aria-label="Jersey coastline with a sandy cove and blue sea"></div>
      <figcaption class="deal__caption">2 nights Jersey Break<br>including flights from £99</figcaption>
    </figure>

    <figure class="deal deal--theatre">
      <div class="deal__visual" role="img" aria-label="Musical theatre poster artwork in green and white"></div>
      <figcaption class="deal__caption">5* London Theatre Break from £150</figcaption>
    </figure>

    <figure class="deal deal--savings">
      <div class="deal__visual" role="img" aria-label="Magnifying glass over the words savings and discount, tinted pink"></div>
      <figcaption class="deal__caption">Millions of people pay over the odds<br>on their holidays by missing out on<br>promotions that are available, but<br>may not be obvious to the customers.</figcaption>
    </figure>

    <p class="band band--promise">We will be scouring the web for you and list the<br>available promo codes which will help you save your<br>hard earned cash!</p>
  </main>

  <p class="dispose-note">Please dispose of this flyer responsibly</p>

  <svg class="recycle" viewBox="0 0 56 48" aria-label="Recycling symbol" role="img">
    <g fill="none" stroke="var(--recycle)" stroke-width="6" stroke-linejoin="round">
      <path d="M22 8 L12 25"/>
      <path d="M34 8 L44 25"/>
      <path d="M14 40 L40 40"/>
    </g>
    <g fill="var(--recycle)">
      <polygon points="26,2 36,6 30,14"/>
      <polygon points="48,30 42,38 38,28"/>
      <polygon points="6,34 16,30 12,44"/>
    </g>
  </svg>
</div>
</body>
</html>
```